Vell & Thorn Website Creation For Online Spirits Sales via MirrowDistillery.com

Want a Website developed that I will use to partner with Mirrow Distillery to sell my signature rum online. Mirrow Distillery will add the final code to make the website an e-commerce site. Website should have links to Social media pages, recipies, About, news and events, products. I have he domain name already just need a designer to make the website look professional. Need website capable of being viewed on iPhone and Android devices. Please use the color scheme that is on the label. The brand motto is: Celebrate Life With Family old and new friends. The bottle sent in the images will be replaced with and actual high resolution image of the bottle when it is produce on 27 DEC 21. Can give the selected designer access to develop the website. I have the hostiveno.com domain name. Final code will be added by a designer from MirrowDistillery.com to make it a e-commerce store.
Updates

I added more information to refine the design I wanted. I should have had this information available to the designers when I started the project.

Target Market(s)

Target Market is 25-50 year old who drink rum

Industry/Entity Type

Spirits. Using Website to sell Rum online

Number of Pages Required

1 page

Font styles to use
Sans Serif

Colors
00AB8E
00BBA5
67D7C9
C6EFE9
E9F9F6

Requirements
Must have
• Must look elegant and of high class. Rum is being market as a premium unnamed rum.
Nice to have
• Video of people drinking, smiling and celebrating

```html
<!DOCTYPE html>
<html lang="en">
<head>
<meta charset="utf-8">
<title>Vell &amp; Thorn — Premium Rum</title>
<link href="https://fonts.googleapis.com/css2?family=Cinzel:wght@400;600&family=Montserrat:wght@400;500;600;700;800&family=Parisienne&display=swap" rel="stylesheet">
<style>
:root{
  --teal:#00AB8E;
  --teal-2:#00BBA5;
  --teal-3:#67D7C9;
  --teal-4:#C6EFE9;
  --teal-5:#E9F9F6;
  --ink:#1b1b1b;
  --body:#555;
  --white:#fff;
  --orange-a:#dd5a1c;
  --orange-b:#f0922f;
  --wood-a:#f1f1f1;
  --wood-b:#dcdcdc;
  --dark:#141414;
}
*{margin:0;padding:0;box-sizing:border-box}
html,body{width:1200px;height:3767px;overflow:hidden;background:var(--white)}
body{position:relative;font-family:"Montserrat",sans-serif;color:var(--ink)}
.abs{position:absolute}
.ph{position:absolute}
.accent{color:var(--teal);font-weight:500}
.strong{font-weight:800;color:var(--ink)}

/* hero */
.hero{position:absolute;left:0;top:0;width:1200px;height:730px;overflow:hidden}
.hero .ph{inset:0;background:linear-gradient(180deg,#2a2d33 0%,#5b6470 45%,#8f969e 70%,#c7b89a 100%)}
.nav{position:absolute;top:0;left:0;width:1200px;height:80px}
.brand{position:absolute;left:111px;top:22px;display:flex;align-items:center;gap:10px;color:var(--white);font-family:"Cinzel",serif;font-size:29px;font-weight:600;letter-spacing:.5px}
.brand .dot{width:38px;height:38px;border:2px solid var(--white);border-radius:50%}
.nav a{position:absolute;top:33px;color:var(--white);font-size:12px;font-weight:500;text-decoration:none;letter-spacing:.3px}
.nav a.active{font-weight:700}
.nav a.active::after{content:"";position:absolute;left:0;right:0;bottom:-8px;height:2px;background:var(--teal)}
.hero-title{position:absolute;left:0;width:1200px;text-align:center;color:var(--white);font-family:"Cinzel",serif}
.hero-title.sm{top:268px;font-size:52px;letter-spacing:3px}
.hero-title.lg{top:318px;font-size:86px;font-weight:600;letter-spacing:2px}

/* headings */
.sec-title{position:absolute;left:0;width:1200px;text-align:center;font-size:32px}
.rule{position:absolute;height:3px;width:66px;background:var(--teal)}

/* about */
.about-frame{left:136px;top:845px;width:396px;height:377px;border:2px solid var(--teal-3)}
.about-photo{left:147px;top:856px;width:374px;height:355px;background:linear-gradient(135deg,#6b8e2a,#c98a2a 45%,#7a4a1a)}
.about-bottle{left:465px;top:982px;width:92px;height:268px;border-radius:30px 30px 14px 14px;background:linear-gradient(90deg,#b86a1c,#e8a246 50%,#b86a1c)}
.about h2{position:absolute;left:612px;top:850px;font-size:35px;font-weight:500;color:var(--teal)}
.about p{position:absolute;left:615px;width:520px;font-size:16.5px;line-height:28px;color:var(--body)}
.btn-teal{position:absolute;background:var(--teal);color:var(--white);font-weight:700;border-radius:30px;display:flex;align-items:center;justify-content:center}

/* products */
.products{position:absolute;left:0;top:1374px;width:1200px;height:703px;background:repeating-linear-gradient(90deg,var(--wood-a) 0 86px,var(--wood-b) 86px 88px)}
.script{position:absolute;left:0;width:1200px;text-align:center;font-family:"Parisienne",cursive;font-size:34px;color:#444}
.prod{position:absolute;width:280px;text-align:center}
.prod .bottle{position:absolute;left:95px;width:90px;height:265px;border-radius:34px 34px 16px 16px}
.prod h3{position:absolute;left:0;width:280px;font-size:16px;font-weight:700}
.prod p{position:absolute;left:0;width:280px;font-size:11.5px;color:#444}
.btn-line{position:absolute;left:70px;width:140px;height:36px;border:2px solid var(--ink);border-radius:20px;font-size:11px;font-weight:800;display:flex;align-items:center;justify-content:center}
.prod-feature{left:447px;top:238px;width:308px;height:350px;background:linear-gradient(160deg,#3a3a3a,#0e0e0e)}
.prod-feature::after{content:"";position:absolute;inset:9px;border:1px solid rgba(255,255,255,.7)}

/* recipes */
.recipes{position:absolute;left:0;top:2077px;width:1200px;height:580px;background:linear-gradient(90deg,var(--orange-a),var(--orange-b))}
.recipe{position:absolute;top:171px;width:462px;height:296px;border-radius:58px 0 58px 0;overflow:hidden;background:#0c0c0c}
.recipe .ph{right:0;top:0;width:250px;height:296px}
.recipe h3{position:absolute;left:47px;top:53px;font-size:20px;font-weight:700;color:var(--white)}
.recipe ul{position:absolute;left:47px;top:97px;list-style:none;color:var(--white);font-size:12.5px;font-weight:500;line-height:25px}
.recipe .btn-teal{left:41px;top:212px;width:130px;height:34px;font-size:11px}

/* news */
.news-card{position:absolute;top:2800px;width:308px;height:340px}
.news-card .ph{left:0;top:0;width:308px;height:205px}
.news-box{position:absolute;left:16px;top:175px;width:280px;height:165px;background:var(--white);border:1px solid #ddd;text-align:center}
.pill{position:absolute;left:94px;top:-10px;width:104px;height:24px;border-radius:12px;background:var(--teal-4);color:var(--teal);font-size:11px;font-weight:600;display:flex;align-items:center;justify-content:center}
.news-box h4{margin-top:34px;font-size:14px;font-weight:500;line-height:19px}
.news-box p{margin-top:8px;font-size:10.5px;color:#777;line-height:15px}
.news-box .more{margin-top:10px;font-size:12px;font-weight:700;color:var(--teal)}

/* footer */
.footer{position:absolute;left:0;top:3226px;width:1200px;height:541px}
.footer .col-rule{position:absolute;top:3360px;width:1px;height:230px;background:rgba(255,255,255,.35)}
.footer-brand{position:absolute;left:80px;width:346px;text-align:center;color:var(--white)}
.f-h{position:absolute;top:3385px;font-family:"Cinzel",serif;font-size:17px;color:var(--white);letter-spacing:.5px}
.f-link{position:absolute;font-size:12.5px;color:var(--white)}
.social{position:absolute;top:3511px;width:34px;height:34px;border:2px solid var(--white);border-radius:50%}
.copy{position:absolute;left:0;top:3692px;width:1200px;text-align:center;font-size:11px;color:var(--white)}
</style>
</head>
<body>

<!-- HERO -->
<section class="hero">
  <div class="ph" role="img" aria-label="Bartender pouring a rum cocktail from a shaker into a glass on a wooden board"></div>
  <nav class="nav">
    <div class="brand"><span class="dot"></span>VELL &amp; THORN</div>
    <a class="active" style="left:472px">ABOUT US</a>
    <a style="left:605px">PRODUCTS</a>
    <a style="left:740px">RECIPIES</a>
    <a style="left:859px">NEWS &amp; EVENT</a>
    <svg class="abs" style="left:1005px;top:30px" width="18" height="18" viewBox="0 0 18 18" fill="none" stroke="#fff" stroke-width="1.6"><circle cx="7.5" cy="7.5" r="5.5"/><path d="M11.5 11.5L16 16"/></svg>
    <svg class="abs" style="left:1052px;top:29px" width="17" height="19" viewBox="0 0 17 19" fill="none" stroke="#fff" stroke-width="1.6"><rect x="1.5" y="5" width="14" height="12.5" rx="1"/><path d="M5 5V3.5a3.5 3.5 0 0 1 7 0V5"/></svg>
  </nav>
  <svg class="abs" style="left:565px;top:196px" width="70" height="70" viewBox="0 0 70 70"><circle cx="35" cy="35" r="33" fill="none" stroke="#fff" stroke-width="2"/><path d="M28 22L49 35L28 48Z" fill="#fff"/></svg>
  <div class="hero-title sm">WELCOME TO</div>
  <div class="hero-title lg">VELL &amp; THORN</div>
  <svg class="abs" style="left:93px;top:337px" width="24" height="40" viewBox="0 0 24 40" fill="none" stroke="#fff" stroke-width="4"><path d="M20 3L4 20L20 37"/></svg>
  <svg class="abs" style="left:1118px;top:337px" width="24" height="40" viewBox="0 0 24 40" fill="none" stroke="#fff" stroke-width="4"><path d="M4 3L20 20L4 37"/></svg>
  <svg class="abs" style="left:0;top:640px" width="1200" height="90" viewBox="0 0 1200 90"><path d="M0 40C220 10 380 30 600 52C820 74 1000 60 1200 20V90H0Z" fill="#fff"/><path d="M0 40C220 10 380 30 600 52C820 74 1000 60 1200 20" fill="none" stroke="#222" stroke-width="3"/></svg>
</section>

<!-- ABOUT -->
<section class="about">
  <div class="ph about-frame"></div>
  <div class="ph about-photo" role="img" aria-label="Glass of rum on ice with lime wedges"></div>
  <div class="ph about-bottle" role="img" aria-label="Vell and Thorn rum bottle"></div>
  <h2>ABOUT <span class="strong">VELL &amp; THORN</span></h2>
  <div class="rule" style="left:614px;top:903px"></div>
  <p style="top:926px">Lorem ipsum dolor sit amet, consectetur adipiscing elit, sed do eiusmod tempor incididunt ut labore et dolore magna aliqua. Ut enim ad minim veniam, quis nostrud exercitation ullamco laboris nisi ut aliquip x ea commodo consequat.</p>
  <p style="top:1062px">Duis aute irure dolor in reprehenderit in voluptate velit esse cillumectetur adipiscing elit, sed do eiusmod tempor</p>
  <div class="btn-teal" style="left:612px;top:1148px;width:202px;height:52px;font-size:15px">LEARN MORE</div>
</section>

<!-- PRODUCTS -->
<section class="products">
  <div class="script" style="top:22px">Shop now</div>
  <div class="sec-title" style="top:63px"><span class="accent">OUR</span> <span class="strong">PRODUCTS</span></div>
  <div class="rule" style="left:567px;top:112px"></div>
  <div class="ph prod-feature"></div>
  <svg class="abs" style="left:84px;top:330px" width="24" height="40" viewBox="0 0 24 40" fill="none" stroke="#777" stroke-width="4"><path d="M20 3L4 20L20 37"/></svg>
  <svg class="abs" style="left:1117px;top:330px" width="24" height="40" viewBox="0 0 24 40" fill="none" stroke="#777" stroke-width="4"><path d="M4 3L20 20L4 37"/></svg>

  <div class="prod" style="left:148px;top:168px">
    <div class="bottle" role="img" aria-label="Red rum bottle" style="top:0;background:linear-gradient(90deg,#b32a1a,#e8503a 50%,#b32a1a)"></div>
    <h3 style="top:301px">VELL &amp; THORN RUM</h3>
    <p style="top:327px">Lorem ipsum dolor sit amet conse</p>
    <div class="btn-line" style="top:355px">SHOP NOW</div>
  </div>
  <div class="prod" style="left:462px;top:168px">
    <div class="bottle" role="img" aria-label="Amber rum bottle beside a glass of rum on ice" style="top:0;background:linear-gradient(90deg,#b86a1c,#eaa545 50%,#b86a1c)"></div>
    <h3 style="top:301px;color:#fff">VELL &amp; THORN RUM</h3>
    <p style="top:327px;color:#ddd">Lorem ipsum dolor sit amet conse</p>
    <div class="btn-line" style="top:355px;border-color:#fff;color:#fff">SHOP NOW</div>
  </div>
  <div class="prod" style="left:779px;top:168px">
    <div class="bottle" role="img" aria-label="Dark amber rum bottle" style="top:0;background:linear-gradient(90deg,#94501c,#c97a35 50%,#94501c)"></div>
    <h3 style="top:301px">VELL &amp; THORN RUM</h3>
    <p style="top:327px">Lorem ipsum dolor sit amet conse</p>
    <div class="btn-line" style="top:367px">SHOP NOW</div>
  </div>
</section>

<!-- RECIPES -->
<section class="recipes">
  <div class="sec-title" style="top:77px;color:#fff"><span style="font-weight:500">OUR</span> <span style="font-weight:800">RECIEPES</span></div>
  <div class="rule" style="left:567px;top:120px;background:#fff"></div>
  <svg class="abs" style="left:82px;top:300px" width="24" height="40" viewBox="0 0 24 40" fill="none" stroke="#fff" stroke-width="4"><path d="M20 3L4 20L20 37"/></svg>
  <svg class="abs" style="left:1108px;top:300px" width="24" height="40" viewBox="0 0 24 40" fill="none" stroke="#fff" stroke-width="4"><path d="M4 3L20 20L4 37"/></svg>
  <div class="recipe" style="left:133px">
    <div class="ph" role="img" aria-label="Rum cocktail on ice with lime" style="background:linear-gradient(90deg,#0c0c0c,#9a6422 40%,#d39a3a)"></div>
    <h3>CRANBERRY THORN</h3>
    <ul><li>Pour all ingredients in a shaker</li><li>Shake vigorously 10 seconds</li><li>Pour Mix in Highball Glass</li><li>Garnish Orange wedge</li></ul>
    <div class="btn-teal">LEARN MORE</div>
  </div>
  <div class="recipe" style="left:614px">
    <div class="ph" role="img" aria-label="Old fashioned cocktail with orange peel and ice" style="background:linear-gradient(90deg,#0c0c0c,#7a4a1c 40%,#c88a3a)"></div>
    <h3>OLD FASHION VELL</h3>
    <ul><li>Pour all ingredients in a shaker</li><li>Shake vigorously 10 seconds</li><li>Pour in glass/ Ice ball</li><li>Garnish w/Orange skin</li></ul>
    <div class="btn-teal">LEARN MORE</div>
  </div>
</section>

<!-- NEWS -->
<section class="news">
  <div class="sec-title" style="top:2707px"><span class="accent">NEWS &amp;</span> <span class="strong">EVENTS</span></div>
  <div class="rule" style="left:570px;top:2754px"></div>
  <div class="news-card" style="left:136px">
    <div class="ph" role="img" aria-label="Distillery tanks under a shed" style="background:linear-gradient(180deg,#8fb4d6,#6a6e70 55%,#4c5a3a)"></div>
    <div class="news-box"><div class="pill">DEC 06, 2021</div><h4>Lorem Ipsum is simply dummy<br>text of the printing</h4><p>Lorem ipsum dolor sit amet, consectetur<br>adipiscing elit, sed do eiusmod tempor</p><div class="more">LEARN MORE &#8594;</div></div>
  </div>
  <div class="news-card" style="left:460px">
    <div class="ph" role="img" aria-label="Rum barrels under palm trees" style="background:linear-gradient(180deg,#cfe3ef,#3f6b3a 45%,#6a5040)"></div>
    <div class="news-box"><div class="pill">DEC 06, 2021</div><h4>Lorem Ipsum is simply dummy<br>text of the printing</h4><p>Lorem ipsum dolor sit amet, consectetur<br>adipiscing elit, sed do eiusmod tempor</p><div class="more">LEARN MORE &#8594;</div></div>
  </div>
  <div class="news-card" style="left:784px">
    <div class="ph" role="img" aria-label="Glasses and bottle of rum on a dark table" style="background:linear-gradient(135deg,#2a2a2a,#6a2a10 55%,#1a1a1a)"></div>
    <div class="news-box"><div class="pill">DEC 06, 2021</div><h4>Lorem Ipsum is simply dummy<br>text of the printing</h4><p>Lorem ipsum dolor sit amet, consectetur<br>adipiscing elit, sed do eiusmod tempor</p><div class="more">LEARN MORE &#8594;</div></div>
  </div>
</section>

<!-- FOOTER -->
<footer>
  <svg class="footer" viewBox="0 0 1200 541" preserveAspectRatio="none">
    <defs><linearGradient id="footGrad" x1="0" y1="0" x2="1" y2="1"><stop offset="0" stop-color="#00BBA5"/><stop offset="1" stop-color="#00AB8E"/></linearGradient></defs>
    <path d="M0 30C260 70 520 30 760 4C940 -8 1080 14 1200 40V541H0Z" fill="url(#footGrad)"/>
    <path d="M0 18C260 50 500 16 760 0" fill="none" stroke="#00BBA5" stroke-width="5"/>
    <rect x="0" y="519" width="1200" height="22" fill="#009c83"/>
  </svg>
  <div class="col-rule" style="left:422px"></div>
  <div class="col-rule" style="left:662px"></div>
  <div class="col-rule" style="left:879px"></div>
  <div class="footer-brand" style="top:3372px"><div style="width:68px;height:68px;border:3px solid #fff;border-radius:50%;margin:0 auto"></div></div>
  <div class="footer-brand" style="top:3450px;font-family:'Cinzel',serif;font-size:33px;font-weight:600">VELL &amp; THORN</div>
  <div class="social" role="img" aria-label="Social link" style="left:173px"></div>
  <div class="social" role="img" aria-label="Social link" style="left:217px"></div>
  <div class="social" role="img" aria-label="Social link" style="left:262px"></div>
  <div class="social" role="img" aria-label="Social link" style="left:306px"></div>

  <div class="f-h" style="left:453px">QUICK LINKS</div>
  <div class="f-link" style="left:458px;top:3429px">About Us</div>
  <div class="f-link" style="left:458px;top:3458px">Receipes</div>
  <div class="f-link" style="left:458px;top:3487px">Products</div>
  <div class="f-link" style="left:458px;top:3516px">News &amp; Events</div>

  <div class="f-h" style="left:700px">RESOURCES</div>
  <div class="f-link" style="left:700px;top:3429px">Shipping &amp; Return</div>
  <div class="f-link" style="left:700px;top:3458px">Support</div>
  <div class="f-link" style="left:700px;top:3487px">Privacy Policy</div>
  <div class="f-link" style="left:700px;top:3516px">Contact</div>

  <div class="f-h" style="left:914px">CONTACT US</div>
  <svg class="abs" style="left:919px;top:3428px" width="16" height="22" viewBox="0 0 16 22"><path d="M8 1a7 7 0 0 0-7 7c0 5 7 13 7 13s7-8 7-13a7 7 0 0 0-7-7z" fill="#fff"/><circle cx="8" cy="8" r="2.6" fill="#00AB8E"/></svg>
  <div class="f-link" style="left:949px;top:3429px;line-height:17px">48 Harrow Mill Lane<br>Brookfield, IL 60599</div>
  <svg class="abs" style="left:919px;top:3476px" width="18" height="18" viewBox="0 0 24 24"><path d="M6.6 10.8a15 15 0 0 0 6.6 6.6l2.2-2.2a1 1 0 0 1 1-.25 11.4 11.4 0 0 0 3.6.57 1 1 0 0 1 1 1V20a1 1 0 0 1-1 1A17 17 0 0 1 3 4a1 1 0 0 1 1-1h3.5a1 1 0 0 1 1 1c0 1.25.2 2.45.57 3.6a1 1 0 0 1-.25 1z" fill="#fff"/></svg>
  <div class="f-link" style="left:949px;top:3478px">(555) 014-2290</div>
  <svg class="abs" style="left:919px;top:3515px" width="19" height="14" viewBox="0 0 19 14"><rect width="19" height="14" rx="1.5" fill="#fff"/><path d="M1 1.5l8.5 6.5L18 1.5" fill="none" stroke="#00AB8E" stroke-width="1.4"/></svg>
  <div class="f-link" style="left:949px;top:3514px">hello@vellandthorn.example</div>

  <div class="copy">© 2021 Vell &amp; Thorn | All Rights Reserved</div>
</footer>

</body>
</html>
```